Quorvane Learning App for Children with Dyslexia

Project Description:

We are seeking a talented UI/UX designer to create engaging and intuitive designs for Quorvane, an innovative educational app designed to help children learn letters and words through a multisensory learning approach. The app aims to be particularly helpful for children with dyslexia, providing a supportive and interactive learning environment.

Key App Features & Design Requirements:

Account Creation Screen: Design a welcoming and straightforward sign-up page that allows users to register with their email or continue with Brindlewave. The design should be clean, focusing on user-friendliness and accessibility, adhering to our terms of service and privacy policy.

Main Screen Design: The main screen should allocate at least 4/6 of its height to the interactive drawing area. It needs to display word prompts in both correct and scrambled orders and include options to "Show all Words," "Play all words," and a search function. The interface should be vibrant, engaging, and easy to navigate for children.

Profile Section: Create a user-friendly profile page that allows users to edit their profile image, name, username, email, links, and bio. The design should be clean and encourage user engagement.

QuorTally Page: This section will display the user's learning progress, including rankings, a learning curve, and recently learned words. It should visually represent progress in a motivating and understandable way, suitable for a younger audience.

Visual and Auditory Feedback Implementation: Incorporate elements that support visual and auditory feedback, using dyslexia-friendly formats. This includes choosing appropriate colors, fonts, and auditory cues.

Accessibility and Customization Settings: Designs should include settings for adjusting visual contrast, font size, and the word list to accommodate individual preferences and needs.

Feel free to add more interactions and/or pages.

Design preferences:

Color Scheme: Use a bright, inviting color palette that stimulates learning and engagement without overwhelming the users.
Font Selection: Opt for fonts that are readable and accessible, particularly for users with dyslexia.
Icons and Graphics: Design custom icons and graphics that are cohesive with the app's theme and purpose. Illustrations should be simple, relatable, and supportive of the learning process.

Target Market(s)

Educational

Industry/Entity Type

Educational

Colors
0054AA
0677BA
7BADD7
CADEEF
E8F1F8
0094D4
00A9DD
6FCCEA
C7EBF8
E9F6FB

Requirements
Must have
• Educational app, a writing area, scoring and account management
Nice to have
• Statistics, Ranking Page, Settings and some nice visual features

```html
<!DOCTYPE html>
<html lang="en">
<head>
<meta charset="utf-8">
<title>Quorvane – App Screens</title>
<link rel="stylesheet" href="https://fonts.googleapis.com/css2?family=Poppins:wght@400;500;600&family=Sniglet:wght@400;800&display=swap">
<style>
:root{
  --page:#efefef;
  --ink:#222;
  --muted:#666;
  --line:#e3e3e3;
  --white:#fff;
  --green:#6ccb00;
  --green-btn:#5cc10a;
  --sky:#6bbcf5;
  --sky-deep:#2ea8f0;
  --purple:#c977f2;
  --purple-deep:#b65ef0;
  --lilac:#d98af5;
  --cyan:#3fc4f5;
  --orange:#ff7a12;
  --orange-soft:#ff9a1c;
  --amber:#f7b300;
  --yellow:#f8c800;
  --navy:#2350b0;
  --blue:#2f78d0;
  --word-orange:#f9a800;
  --tag-yellow:#f8e21b;
  --lime:#8fd800;
}
*{box-sizing:border-box;margin:0;padding:0}
html,body{width:1058px;height:1200px;overflow:hidden}
body{background:var(--page);font-family:"Poppins",sans-serif;color:var(--ink);position:relative}
.screen-title{position:absolute;width:260px;text-align:center;font-size:17px;font-weight:400;color:#333}
.screen{position:absolute;width:189px;height:414px;border-radius:26px;overflow:hidden}
.status{position:absolute;top:0;left:0;right:0;height:26px;display:flex;justify-content:space-between;align-items:center;padding:6px 10px 0 12px;font-size:10px}
.status .icons{display:flex;gap:3px;align-items:center}
.appbar{position:absolute;top:26px;left:0;right:0;height:36px;display:flex;align-items:center;justify-content:center;color:#fff;font-family:"Sniglet",sans-serif;font-weight:800;font-size:13px}
.appbar .left{position:absolute;left:8px;top:12px}
.appbar .right{position:absolute;right:7px;font-family:"Poppins",sans-serif;font-size:6px;font-weight:600}
.frame{position:absolute;left:5px;right:5px;border:1.5px solid rgba(255,255,255,.85);border-radius:4px}
.card{position:absolute;left:10px;right:10px;background:var(--white);border-radius:3px}
/* login */
.login{background:var(--green)}
.login .card{top:38px;height:344px;text-align:center;padding-top:16px}
.brand{font-family:"Sniglet",sans-serif;font-weight:800;font-size:19px;color:#111}
.tagline{font-size:6px;margin-top:1px}
.art{margin:8px auto 0;width:158px;height:100px;border-radius:50% 50% 8px 8px;background:linear-gradient(#eef6fb,#dcebb0 70%,#b9d94a)}
.heading{font-family:"Sniglet",sans-serif;font-size:12px;color:#1d2a55;margin-top:12px}
.sub{font-size:6px;color:#555;margin-top:4px}
.input{margin:7px 6px 0;height:23px;background:#f1f1f1;border-radius:3px;font-size:6px;color:#555;text-align:left;padding:8px 8px}
.btn{margin:4px 6px 0;height:23px;border-radius:3px;font-size:7px;display:flex;align-items:center;justify-content:center;gap:6px}
.btn.primary{background:var(--green-btn);color:#fff}
.btn.ghost{background:#f1f1f1;color:#222}
.or{font-size:6px;color:#555;margin-top:7px}
.dot{width:9px;height:9px;border-radius:50%;background:#4a8af4}
.terms{font-size:6px;color:#555;margin-top:14px;line-height:1.3}
.terms b{font-weight:400;color:#222}
/* profile */
.profile{background:linear-gradient(var(--sky) 0 190px,var(--sky-deep))}
.profile .appbar{background:var(--sky)}
.profile .stripe{position:absolute;top:62px;left:0;right:0;height:4px;background:var(--sky-deep)}
.profile .frame{top:74px;bottom:24px}
.profile .card{top:80px;height:303px;padding:7px 8px}
.avatar{width:46px;height:46px;border-radius:50%;margin:0 auto;background:linear-gradient(#cfd3d6,#9aa0a6);position:relative}
.avatar .cam{position:absolute;right:-2px;bottom:0;width:13px;height:13px;border-radius:50%;background:var(--amber);border:1.5px solid #fff}
.edit-label{text-align:center;font-size:9px;margin-top:8px;font-weight:500}
.row{display:flex;align-items:flex-start;gap:8px;border-bottom:1px solid var(--line);padding:5px 2px 6px;position:relative}
.row .ico{width:7px;height:7px;border-radius:2px;background:#999;margin-top:2px}
.row .lab{font-size:5px;color:#666}
.row .val{font-size:6.5px;font-weight:500;line-height:1.6}
.row .chev{position:absolute;right:4px;top:11px;font-size:7px}
.add{color:var(--orange);font-size:6px}
.elephant{position:absolute;right:8px;bottom:6px;width:48px;height:44px;border-radius:45%;background:linear-gradient(#c9dbe8,#9fb9cc)}
/* stats */
.stats{background:var(--purple)}
.stats .appbar{background:var(--purple-deep)}
.stats .frame{top:72px;bottom:22px}
.tabs{position:absolute;top:78px;left:12px;right:6px;display:flex;gap:4px}
.tab{height:20px;border-radius:10px;font-size:6.5px;color:#fff;display:flex;align-items:center;padding:0 9px;background:rgba(255,255,255,.3)}
.tab.on{background:var(--cyan)}
.ranks{position:absolute;top:107px;left:10px;display:flex;gap:4px}
.rank{width:104px;height:42px;border-radius:3px;color:#fff;padding:7px 6px;overflow:hidden;white-space:nowrap}
.rank small{font-size:5.5px;display:block}
.rank strong{font-size:12px;font-weight:500}
.rank.total{background:var(--amber)}
.rank.daily{background:var(--lime)}
.stats .curve{top:158px;height:128px;padding:8px 6px}
.stats .recent{top:294px;height:86px;padding:8px 6px}
.panel-title{font-size:8.5px;font-weight:500}
.recent ul{list-style:none;margin-top:4px}
.recent li{font-size:6.5px;color:#444;border-bottom:1px solid var(--line);padding:2px 0 3px}
.recent li:last-child{border:0}
/* main */
.main .frame{top:72px;bottom:24px}
.draw{top:78px;height:131px;display:flex;align-items:center;justify-content:center;font-size:9px;font-weight:500}
.tools{position:absolute;display:flex;gap:3px}
.tool{width:13px;height:13px;border-radius:50%;display:flex;align-items:center;justify-content:center;color:#fff;font-size:8px;line-height:1}
.t-del{background:#62c42a}.t-pen{background:#27a6ee}.t-x{background:#d07be8}.t-pal{background:var(--amber)}
.play{top:214px;height:168px;padding:10px 5px}
.actions{display:flex;gap:5px;padding:0 1px}
.action{flex:1;height:31px;border-radius:3px;font-size:6px;display:flex;align-items:center;justify-content:center;gap:4px}
.words{display:grid;grid-template-columns:repeat(3,48px);gap:5px 5px;margin-top:11px;padding-left:1px}
.word{height:28px;border-radius:3px;color:#fff;font-size:7px;display:flex;align-items:center;justify-content:center}
.giraffe{position:absolute;right:6px;top:90px;width:40px;height:78px;border-radius:40% 40% 6px 6px;background:linear-gradient(#ffc766,#f3a23a)}
.results{position:absolute;left:6px;right:6px;bottom:11px;height:25px;border-radius:3px;color:#fff;font-size:7px;display:flex;align-items:center;justify-content:center}
.v1{background:linear-gradient(var(--navy),var(--blue))}
.v1 .appbar{background:var(--navy);border-bottom:3px solid #1d43a0}
.v2{background:var(--orange-soft)}
.v2 .appbar{background:var(--orange);border-bottom:3px solid #ff6a00}
.v3{background:var(--yellow)}
.v3 .appbar{background:var(--amber);border-bottom:3px solid #f5a800}
</style>
</head>
<body>

<div class="screen-title" style="left:107px;top:70px">Login</div>
<div class="screen-title" style="left:377px;top:70px">Profile</div>
<div class="screen-title" style="left:658px;top:70px">QuorTally</div>
<div class="screen-title" style="left:107px;top:605px">Main Screen Sample 1</div>
<div class="screen-title" style="left:377px;top:605px">Main Screen Sample 2</div>
<div class="screen-title" style="left:658px;top:605px">Main Screen Sample 3</div>

<!-- Login -->
<section class="screen login" style="left:143px;top:124px">
  <div class="status"><span>9:41</span><span class="icons"><svg width="22" height="7"><rect x="0" y="4" width="2" height="3" fill="#111"/><rect x="3" y="2.5" width="2" height="4.5" fill="#111"/><rect x="6" y="1" width="2" height="6" fill="#111"/><rect x="12" y="1" width="10" height="5" rx="1" fill="#111"/></svg></span></div>
  <div class="frame" style="top:33px;bottom:26px"></div>
  <div class="card">
    <div class="brand">Quorvane</div>
    <div class="tagline">Learn letters and words</div>
    <div class="art" role="img" aria-label="Illustration of a bear reading a book on a grassy patch"></div>
    <div class="heading">Create An Account</div>
    <div class="sub">Enter your email to sign up for this app</div>
    <div class="input">Email Address</div>
    <div class="btn primary">Sign up with email</div>
    <div class="or">or continue with</div>
    <div class="btn ghost" style="margin-top:7px"><span class="dot"></span>Login with Brindlewave</div>
    <div class="terms">By clicking continue, you agree to our<br><b>Terms of Service</b> and <b>Privacy Policy</b></div>
  </div>
</section>

<!-- Profile -->
<section class="screen profile" style="left:413px;top:124px">
  <div class="status"><span>9:41</span><span class="icons"><svg width="22" height="7"><rect x="0" y="4" width="2" height="3" fill="#111"/><rect x="3" y="2.5" width="2" height="4.5" fill="#111"/><rect x="6" y="1" width="2" height="6" fill="#111"/><rect x="12" y="1" width="10" height="5" rx="1" fill="#111"/></svg></span></div>
  <div class="appbar"><span class="left" style="top:12px">‹</span>Profile</div>
  <div class="stripe"></div>
  <div class="frame"></div>
  <div class="card">
    <div class="avatar" role="img" aria-label="Profile photo of the user"><span class="cam"></span></div>
    <div class="edit-label">Edit profile image</div>
    <div style="margin-top:6px">
      <div class="row"><span class="ico"></span><div><div class="lab">Name</div><div class="val">Mira Solden</div></div><span class="chev">›</span></div>
      <div class="row"><span class="ico"></span><div><div class="lab">Username</div><div class="val">@username</div></div><span class="chev">›</span></div>
      <div class="row"><span class="ico"></span><div><div class="lab">Email</div><div class="val">name@mailvale.com</div></div><span class="chev">›</span></div>
      <div class="row"><span class="ico"></span><div><div class="lab">Links</div><div class="val">pagefold.net<br>linkmere.net<br>tidelink.net</div><div class="add">+Add link</div></div></div>
      <div class="row" style="border:0"><span class="ico"></span><div><div class="lab">Bio</div><div class="val">A description of this user.</div></div><span class="chev">›</span></div>
    </div>
    <div class="elephant" role="img" aria-label="Illustration of an elephant reading a book"></div>
  </div>
</section>

<!-- QuorTally -->
<section class="screen stats" style="left:694px;top:124px">
  <div class="status"><span>9:41</span><span class="icons"><svg width="22" height="7"><rect x="0" y="4" width="2" height="3" fill="#111"/><rect x="3" y="2.5" width="2" height="4.5" fill="#111"/><rect x="6" y="1" width="2" height="6" fill="#111"/><rect x="12" y="1" width="10" height="5" rx="1" fill="#111"/></svg></span></div>
  <div class="appbar"><svg class="left" width="8" height="6"><rect y="0" width="8" height="1" fill="#fff"/><rect y="2.5" width="8" height="1" fill="#fff"/><rect y="5" width="8" height="1" fill="#fff"/></svg>QuorTally<span class="right" style="width:14px;height:14px;border-radius:50%;background:linear-gradient(#e8ddd6,#a89088)" role="img" aria-label="User avatar"></span></div>
  <div class="frame"></div>
  <div class="tabs"><span class="tab on">Ranking</span><span class="tab">Correct Words</span><span class="tab">Todo..</span></div>
  <div class="ranks">
    <div class="rank total"><small>Total Ranking</small><strong>1st Place of 100</strong></div>
    <div class="rank daily"><small>Daily Ranking</small><strong>10th Place</strong></div>
  </div>
  <div class="card curve">
    <div class="panel-title">Learning curve</div>
    <svg width="157" height="100" viewBox="0 0 157 100" style="margin-top:4px">
      <g stroke="#e6e6e6" stroke-width=".6">
        <line x1="0" y1="4" x2="157" y2="4"/><line x1="0" y1="20" x2="157" y2="20"/><line x1="0" y1="37" x2="157" y2="37"/><line x1="0" y1="53" x2="157" y2="53"/><line x1="0" y1="70" x2="157" y2="70"/><line x1="0" y1="86" x2="157" y2="86"/>
      </g>
      <g font-family="Poppins, sans-serif" font-size="5" fill="#777">
        <text x="1" y="12">100 words per day</text><text x="1" y="29">50 words per day</text>
        <text x="1" y="46">......</text><text x="1" y="62">......</text><text x="1" y="79">......</text>
        <text x="1" y="97">Nov</text><text x="19" y="97">23</text><text x="37" y="97">24</text><text x="54" y="97">25</text><text x="71" y="97">26</text><text x="89" y="97">27</text><text x="107" y="97">28</text><text x="125" y="97">29</text><text x="143" y="97">30</text>
      </g>
      <polyline fill="none" stroke="#c06af0" stroke-width="1.3" points="2,84 28,81 52,66 58,70 90,50 96,52 110,37 117,44 126,34 133,37 145,6"/>
      <circle cx="145" cy="6" r="2" fill="#c06af0"/>
    </svg>
  </div>
  <div class="card recent">
    <div class="panel-title">Recently learned words</div>
    <ul><li>El</li><li>ELA</li><li>Lorem</li><li>Lorem</li></ul>
  </div>
</section>

<!-- Main 1 -->
<section class="screen main v1" style="left:143px;top:650px">
  <div class="status" style="color:#fff"><span>9:41</span><span class="icons"><svg width="22" height="7"><rect x="0" y="4" width="2" height="3" fill="#fff"/><rect x="3" y="2.5" width="2" height="4.5" fill="#fff"/><rect x="6" y="1" width="2" height="6" fill="#fff"/><rect x="12" y="1" width="10" height="5" rx="1" fill="#fff"/></svg></span></div>
  <div class="appbar"><svg class="left" width="8" height="6"><rect width="8" height="1" fill="#fff"/><rect y="2.5" width="8" height="1" fill="#fff"/><rect y="5" width="8" height="1" fill="#fff"/></svg>Main Screen<span class="right">16 Points</span></div>
  <div class="frame"></div>
  <div class="card draw">Drawing Area
    <div class="tools" style="top:5px;right:6px"><span class="tool t-x">×</span><span class="tool t-pal">●</span></div>
    <div class="tools" style="bottom:5px;left:5px"><span class="tool t-del">▮</span><span class="tool t-pen">✎</span></div>
  </div>
  <div class="card play">
    <div class="actions">
      <div class="action" style="background:#e8f3fb;border:1px solid #9ccbee;color:#333">◉ Show All Words</div>
      <div class="action" style="background:#27a6ee;color:#fff">▷ Play All Words</div>
    </div>
    <div class="words">
      <div class="word" style="background:var(--word-orange)">Word 1</div><div class="word" style="background:var(--word-orange)">Word 2</div><div class="word" style="background:var(--word-orange)">Word 3</div>
      <div class="word" style="background:var(--word-orange)">Word 4</div><div class="word" style="background:var(--word-orange)">...</div>
    </div>
    <div class="giraffe" role="img" aria-label="Illustration of a giraffe with glasses"></div>
    <div class="results" style="background:var(--green-btn)">Show Me The Results</div>
  </div>
</section>

<!-- Main 2 -->
<section class="screen main v2" style="left:413px;top:650px">
  <div class="status" style="color:#fff"><span>9:41</span><span class="icons"><svg width="22" height="7"><rect x="0" y="4" width="2" height="3" fill="#111"/><rect x="3" y="2.5" width="2" height="4.5" fill="#111"/><rect x="6" y="1" width="2" height="6" fill="#111"/><rect x="12" y="1" width="10" height="5" rx="1" fill="#111"/></svg></span></div>
  <div class="appbar"><svg class="left" width="8" height="6"><rect width="8" height="1" fill="#fff"/><rect y="2.5" width="8" height="1" fill="#fff"/><rect y="5" width="8" height="1" fill="#fff"/></svg>Main Screen<span class="right">16 Points</span></div>
  <div class="frame"></div>
  <div class="card draw">Drawing Area
    <div class="tools" style="top:5px;right:6px"><span class="tool t-del">▮</span><span class="tool t-pen">✎</span><span class="tool t-x">×</span><span class="tool t-pal">●</span></div>
  </div>
  <div class="card play">
    <div class="actions">
      <div class="action" style="background:var(--tag-yellow);color:#222">◉ Show All Words</div>
      <div class="action" style="background:var(--lime);color:#fff">▷ Play All Words</div>
    </div>
    <div class="words">
      <div class="word" style="background:var(--lilac)">Word 1</div><div class="word" style="background:var(--lilac)">Word 2</div><div class="word" style="background:var(--lilac)">Word 3</div>
      <div class="word" style="background:var(--lilac)">Word 4</div><div class="word" style="background:var(--lilac)">...</div>
    </div>
    <div class="giraffe" role="img" aria-label="Illustration of a giraffe with glasses"></div>
    <div class="results" style="background:var(--orange)">Show me the results</div>
  </div>
</section>

<!-- Main 3 -->
<section class="screen main v3" style="left:694px;top:650px">
  <div class="status" style="color:#fff"><span>9:41</span><span class="icons"><svg width="22" height="7"><rect x="0" y="4" width="2" height="3" fill="#111"/><rect x="3" y="2.5" width="2" height="4.5" fill="#111"/><rect x="6" y="1" width="2" height="6" fill="#111"/><rect x="12" y="1" width="10" height="5" rx="1" fill="#111"/></svg></span></div>
  <div class="appbar"><svg class="left" width="8" height="6"><rect width="8" height="1" fill="#fff"/><rect y="2.5" width="8" height="1" fill="#fff"/><rect y="5" width="8" height="1" fill="#fff"/></svg>Main Screen<span class="right">16 Points</span></div>
  <div class="frame"></div>
  <div class="card draw">Drawing Area
    <div class="tools" style="bottom:5px;left:5px"><span class="tool t-del">▮</span><span class="tool t-pen">✎</span><span class="tool t-x">×</span><span class="tool t-pal">●</span></div>
  </div>
  <div class="card play">
    <div class="actions">
      <div class="action" style="background:#fff;border:1px solid #e2b8f5;color:#222"><span style="color:var(--lilac)">◉</span> Show All Words</div>
      <div class="action" style="background:var(--lilac);color:#fff">▷ Play All Words</div>
    </div>
    <div class="words">
      <div class="word" style="background:var(--yellow)">Word 1</div><div class="word" style="background:var(--yellow)">Word 2</div><div class="word" style="background:var(--yellow)">Word 3</div>
      <div class="word" style="background:var(--yellow)">Word 4</div><div class="word" style="background:var(--yellow)">...</div>
    </div>
    <div class="giraffe" role="img" aria-label="Illustration of a giraffe with glasses"></div>
    <div class="results" style="background:var(--green-btn)">Show me the results</div>
  </div>
</section>

</body>
</html>
```